Childcare Centre Franchise Website Design

Our business is Childcare centre, and we are the franchise with 4 centres currently, we would like to have the website similar as the link below,
https://www.maplewren.edu.au/
with the same items, functions and pages. Locations information for all centres, and have pages for each centre. Additionally, we will need a page for online enrolment.
Our logo is attached.

```html
<!DOCTYPE html>
<html lang="en">
<head>
<meta charset="utf-8">
<title>Tiny Sprouts Childcare &amp; Education</title>
<link href="https://fonts.googleapis.com/css2?family=Libre+Baskerville&family=Quicksand:wght@500;600;700&family=Dancing+Script:wght@600&display=swap" rel="stylesheet">
<style>
:root{
  --brown:#7a3e2b;
  --teal:#0f9d98;
  --green:#8dc63f;
  --pink:#d63b6f;
  --grey:#ececec;
  --ink:#2d2d2d;
  --muted:#555;
  --white:#fff;
}
*{box-sizing:border-box;margin:0;padding:0}
html,body{width:1200px;height:3945px;overflow:hidden}
body{position:relative;background:var(--white);font-family:"Quicksand",sans-serif;color:var(--ink)}
.abs{position:absolute}
.serif{font-family:"Libre Baskerville",serif}
.script{font-family:"Dancing Script",cursive}
.center{text-align:center}
.btn-outline{position:absolute;border:1.5px solid var(--teal);color:var(--teal);font-family:"Libre Baskerville",serif;font-size:11px;display:flex;align-items:center;justify-content:center;background:var(--white)}
.site-header{position:absolute;left:0;top:0;width:1200px;height:93px;background:var(--white);z-index:3}
.brand{position:absolute;left:124px;top:66px;font-family:"Libre Baskerville",serif;font-size:17px;color:var(--brown)}
.brand-mark{position:absolute;left:170px;top:8px;width:52px;height:52px;border-radius:50%;background:var(--green);opacity:.8}
.topbar{position:absolute;top:0;height:29px;display:flex;align-items:center;font-size:12px}
.nav{position:absolute;top:54px;font-size:12px;font-weight:600;color:#333}
.hero{position:absolute;left:0;top:93px;width:1200px;height:360px}
.hero-title{position:absolute;top:197px;width:1200px;text-align:center;color:var(--white);font-size:34px;font-weight:400}
.finder-tab{position:absolute;left:378px;top:418px;width:441px;height:31px;background:var(--green);color:var(--white);font-family:"Libre Baskerville",serif;font-size:14px;display:flex;align-items:center;justify-content:center;clip-path:polygon(3% 0,97% 0,100% 100%,0 100%)}
.finder{position:absolute;left:288px;top:449px;width:624px;height:91px;background:var(--brown);border-radius:3px}
.finder input{position:absolute;left:24px;top:23px;width:424px;height:29px;border:0;padding-left:14px;font-family:"Quicksand",sans-serif;font-size:10px}
.finder .search{position:absolute;left:462px;top:23px;width:136px;height:29px;background:var(--teal);color:var(--white);font-size:12px;display:flex;align-items:center;justify-content:center;font-weight:600}
.finder .loc{position:absolute;top:62px;width:624px;text-align:center;color:var(--white);font-size:11px}
.section-title{position:absolute;width:1200px;text-align:center;font-family:"Libre Baskerville",serif;color:var(--brown);font-size:22px;line-height:1.3;font-weight:400}
.support{position:absolute;top:681px;width:210px;text-align:center}
.support .icon{width:56px;height:54px;margin:0 auto;display:block}
.support h3{font-family:"Libre Baskerville",serif;font-weight:400;font-size:15px;margin-top:20px}
.support p{font-size:10.5px;color:var(--muted);line-height:1.45;margin-top:14px;font-weight:500}
.tour{position:absolute;left:199px;top:940px;width:802px;height:282px;background:linear-gradient(90deg,#dfe9e8,#cfe1e2 60%,#e6ecec);border-radius:2px}
.tile{position:absolute;width:182px;height:199px;display:flex;align-items:flex-end;justify-content:center;padding-bottom:22px;color:var(--white);font-family:"Libre Baskerville",serif;font-size:12.5px;text-align:center;line-height:1.3}
.news-img{position:absolute}
.news-title{position:absolute;font-size:13px;font-weight:700;line-height:1.3}
.news-text{position:absolute;font-size:10px;color:var(--muted);line-height:1.45;font-weight:500}
.read{position:absolute;font-family:"Libre Baskerville",serif;color:var(--green);font-size:11px}
.tabs{position:absolute;left:199px;top:2515px;width:802px;height:31px;display:flex}
.tab{flex:1;background:var(--white);display:flex;align-items:center;justify-content:center;font-size:11px;font-weight:700;clip-path:polygon(0 0,100% 0,92% 100%,0 100%);margin-right:-8px}
.tab.active{background:var(--green);color:var(--white)}
.centre{position:absolute;top:2578px;width:182px;height:244px;background:#f4f4f4}
.centre .ph{height:178px}
.centre p{font-size:10.5px;font-weight:700;text-align:center;padding:14px 10px 0;line-height:1.3}
.foot-col{position:absolute;top:3608px;font-size:9.5px;line-height:22.7px;color:#444;font-weight:500}
.social{position:absolute;left:969px;width:30px;height:30px;border-radius:50%}
</style>
</head>
<body>

<header class="site-header">
  <div class="brand-mark"></div>
  <div class="brand">TINY SPROUTS</div>
  <div class="topbar" style="left:732px;width:190px;background:#f2f2f2;justify-content:center;color:var(--brown)">
    <svg width="12" height="12" viewBox="0 0 24 24"><path d="M6.6 10.8a15 15 0 0 0 6.6 6.6l2.2-2.2c.3-.3.7-.4 1-.2 1.1.4 2.3.6 3.6.6.6 0 1 .4 1 1V20c0 .6-.4 1-1 1A17 17 0 0 1 3 4c0-.6.4-1 1-1h3.5c.6 0 1 .4 1 1 0 1.3.2 2.5.6 3.6.1.3 0 .7-.2 1z" fill="#7a3e2b"/></svg>&nbsp;123-456-7890
  </div>
  <div class="topbar" style="left:922px;width:40px;background:var(--brown);justify-content:center">
    <svg width="12" height="12" viewBox="0 0 24 24"><circle cx="10" cy="10" r="6" stroke="#fff" stroke-width="3" fill="none"/><path d="M15 15l6 6" stroke="#fff" stroke-width="3"/></svg>
  </div>
  <div class="topbar serif" style="left:957px;width:138px;background:var(--green);color:#fff;justify-content:center;clip-path:polygon(8% 0,100% 0,100% 100%,0 100%)">Find a Centre</div>
  <nav>
    <span class="nav" style="left:458px">Childcare &amp; Education</span>
    <span class="nav" style="left:608px">Childcare Centres</span>
    <span class="nav" style="left:736px">Childcare Subsidy</span>
    <span class="nav" style="left:865px">News &amp; Advice</span>
    <span class="nav" style="left:974px">Careers</span>
    <span class="nav" style="left:1047px">About Us</span>
  </nav>
</header>

<section class="hero">
  <svg width="1200" height="360" viewBox="0 0 1200 360" class="abs" style="left:0;top:0">
    <defs>
      <linearGradient id="heroFill" x1="0" y1="0" x2="1" y2="1">
        <stop offset="0" stop-color="#5b7a3a"/><stop offset=".5" stop-color="#8a6f5c"/><stop offset="1" stop-color="#4d6a30"/>
      </linearGradient>
    </defs>
    <path d="M0 0H1200V155Q900 330 600 325Q300 330 0 155Z" fill="url(#heroFill)" role="img" aria-label="Photo of smiling children lying on the grass"/>
    <path d="M60 195Q300 335 600 326Q900 335 1140 195Q900 345 600 340Q300 345 60 195Z" fill="#8dc63f"/>
  </svg>
  <h1 class="hero-title serif">Be Creative. Be Brave. Be Curious</h1>
</section>
<div class="finder-tab">Find your Centre to Enrol</div>
<div class="finder">
  <input type="text" placeholder="Enter Postcode or Suburb" aria-label="Postcode or suburb">
  <div class="search">Search</div>
  <div class="loc">Or Use Your Current Location</div>
</div>

<h2 class="section-title" style="top:600px">We’re Here to Support the<br>Whole Family</h2>
<div class="support" style="left:220px">
  <svg class="icon" viewBox="0 0 56 54"><rect x="6" y="18" width="44" height="30" rx="3" fill="none" stroke="#555" stroke-width="2"/><circle cx="28" cy="14" r="11" fill="#f2c230"/><text x="28" y="19" text-anchor="middle" font-size="14" fill="#7a3e2b" font-family="Quicksand">$</text></svg>
  <h3>Child Care Subsidy</h3>
  <p>Our fast &amp; simple Child Care Subsidy Calculator can help you determine what support you’re eligible for.</p>
</div>
<div class="support" style="left:495px">
  <svg class="icon" viewBox="0 0 56 54"><circle cx="28" cy="27" r="24" fill="#8dc63f" opacity=".75"/></svg>
  <h3>Why Wattlebrook?</h3>
  <p>When there are so many childcare options available, how do you know Wattlebrook is the best choice for your family?</p>
</div>
<div class="support" style="left:771px">
  <svg class="icon" viewBox="0 0 56 54"><path d="M30 8c-8-6-18 4-8 14l8 8 8-8c10-10 0-20-8-14z" fill="#8dc63f"/><path d="M6 44h14l10-6h14" stroke="#0f9d98" stroke-width="4" fill="none" stroke-linecap="round"/></svg>
  <h3>Health &amp; Wellbeing</h3>
  <p>The health, safety and wellbeing of our people – big and small – is always our highest priority.</p>
</div>
<div class="btn-outline" style="left:275px;top:845px;width:100px;height:31px">Calculate</div>
<div class="btn-outline" style="left:550px;top:845px;width:100px;height:31px">Learn More</div>
<div class="btn-outline" style="left:826px;top:845px;width:100px;height:31px">Learn More</div>

<svg class="abs" style="left:0;top:1000px" width="1200" height="800" viewBox="0 0 1200 800">
  <path d="M0 70Q300 10 600 60T1200 30V760Q900 720 600 770T0 760Z" fill="var(--grey)"/>
</svg>
<div class="tour" role="img" aria-label="Nursery room with a small table, shelf, toys and a pink armchair with a teddy bear"></div>
<div class="abs script center" style="left:199px;top:986px;width:802px;color:var(--teal);font-size:19px">Book a Tour Now</div>
<div class="abs serif center" style="left:199px;top:1012px;width:802px;font-size:28px;line-height:1.3;color:#222">Limited Spaces Available<br>for 2023</div>
<div class="abs serif" style="left:536px;top:1102px;width:127px;height:31px;background:var(--teal);color:#fff;font-size:11px;display:flex;align-items:center;justify-content:center">Book a Tour Now</div>
<svg class="abs" style="left:580px;top:1185px" width="40" height="12"><circle cx="7" cy="6" r="4" fill="#fff" stroke="#555"/><circle cx="19" cy="6" r="4" fill="#555"/><circle cx="31" cy="6" r="4" fill="#fff" stroke="#555"/></svg>

<div class="abs script" style="left:106px;top:1374px;color:var(--teal);font-size:19px">A love of</div>
<h2 class="abs serif" style="left:106px;top:1414px;width:360px;color:var(--brown);font-size:28px;font-weight:400;line-height:1.3">Learning. Confidence. Curiosity. Here are some of the ways we help children thrive.</h2>
<div class="btn-outline" style="left:106px;top:1580px;width:157px;height:31px;background:transparent">Discover our Approach</div>

<div class="tile" style="left:499px;top:1396px;background:linear-gradient(180deg,#6d8fa8,#2ba3a0)" role="img" aria-label="Children looking at a globe with a teacher">High-Quality<br>Curriculum</div>
<div class="tile" style="left:706px;top:1283px;background:linear-gradient(180deg,#b8a6a8,#d8366e)" role="img" aria-label="Children playing together on the floor">Exciting<br>Environments</div>
<div class="tile" style="left:706px;top:1508px;background:linear-gradient(180deg,#7d7560,#7a3e2b)" role="img" aria-label="Two children smiling outdoors">Wellbeing and<br>Nutrition</div>
<div class="tile" style="left:912px;top:1396px;background:linear-gradient(180deg,#b9a070,#7fbf3a)" role="img" aria-label="Group of children hugging outdoors">Community<br>Connections</div>

<h2 class="section-title" style="top:1858px">Latest News &amp; Advice from<br>Our Team of Experts</h2>
<div class="news-img" style="left:199px;top:1973px;width:182px;height:181px;background:linear-gradient(180deg,#9cb9d6,#d88a3c)" role="img" aria-label="Group of children in colourful shirts"></div>
<div class="news-title" style="left:199px;top:2170px;width:182px">Contrary to popular lorem belief, lorem ipsum</div>
<div class="news-text" style="left:199px;top:2217px;width:182px">There are many variations of passages of lorem Ipsum available, but the majority have suffered alteration ...</div>
<div class="read" style="left:199px;top:2285px">Read More →</div>

<div class="news-img" style="left:430px;top:1943px;width:339px;height:298px;background:linear-gradient(135deg,#c8347a,#6b8a3e 60%,#4c7a2c)" role="img" aria-label="Children lying on the grass in a circle"></div>
<div class="abs" style="left:455px;top:2182px;width:289px;height:115px;background:#fff"></div>
<div class="news-title center" style="left:470px;top:2201px;width:259px">Contrary to popular lorem belief, lorem ipsum</div>
<div class="news-text center" style="left:480px;top:2249px;width:239px">There are many variations of passages of lorem Ipsum available, but the majority have suffered alteration ...</div>
<div class="read center" style="left:455px;top:2302px;width:289px">Read More →</div>

<div class="news-img" style="left:819px;top:1973px;width:182px;height:181px;background:#000" role="img" aria-label="Article image"></div>
<div class="news-title" style="left:819px;top:2170px;width:182px">Contrary to popular lorem belief, lorem ipsum</div>
<div class="news-text" style="left:819px;top:2217px;width:182px">There are many variations of passages of lorem Ipsum available, but the majority have suffered alteration ...</div>
<div class="read" style="left:819px;top:2285px">Read More →</div>

<svg class="abs" style="left:0;top:2380px" width="1200" height="580" viewBox="0 0 1200 580">
  <path d="M0 50Q300 0 600 40T1200 20V520Q900 480 600 530T0 560Z" fill="var(--teal)"/>
</svg>
<h2 class="section-title" style="top:2436px;color:#fff">Find Your Village<br>Childcare Centres by State</h2>
<div class="abs" style="left:106px;top:2530px;width:989px;height:1px;background:rgba(255,255,255,.6)"></div>
<div class="tabs">
  <div class="tab" style="justify-content:flex-start;padding-left:10px">Australian Capital Territory</div>
  <div class="tab">Victoria</div>
  <div class="tab active">New South Wales</div>
  <div class="tab">Queensland</div>
  <div class="tab" style="clip-path:none;margin-right:0">South Australia</div>
</div>
<div class="centre" style="left:199px"><div class="ph" style="background:linear-gradient(180deg,#e8c23a,#d44a3a)" role="img" aria-label="Children on a playground climbing frame"></div><p>Tiny Sprouts Childcare and Education Barangaroo</p></div>
<div class="centre" style="left:406px"><div class="ph" style="background:linear-gradient(180deg,#e6e1d8,#b09a78)" role="img" aria-label="Children at a craft table"></div><p>Tiny Sprouts Childcare and Education Marsfield</p></div>
<div class="centre" style="left:612px"><div class="ph" style="background:linear-gradient(180deg,#6f8f4c,#3f6a2a)" role="img" aria-label="Children playing in a circle on grass"></div><p>Tiny Sprouts Childcare and Education Acacia Gardens</p></div>
<div class="centre" style="left:819px"><div class="ph" style="background:linear-gradient(180deg,#d8c3aa,#2c7bbf)" role="img" aria-label="Teacher with children at a blue table"></div><p>Tiny Sprouts Childcare and Education Rouse Hill North</p></div>
<div class="abs serif" style="left:519px;top:2852px;width:162px;height:31px;border:1.5px solid #fff;color:#fff;font-size:11px;display:flex;align-items:center;justify-content:center">View All NSW Centres</div>

<div class="abs" style="left:0;top:2940px;width:1200px;height:540px;background:linear-gradient(180deg,#d9ebf7 0%,#eef6fb 35%,#9ec27a 70%,#6b9a3e 100%);z-index:-1" role="img" aria-label="Children jumping happily outdoors under trees"></div>
<div class="abs script center" style="left:0;top:3024px;width:1200px;color:var(--teal);font-size:19px">Be Bold</div>
<h2 class="abs serif center" style="left:0;top:3050px;width:1200px;color:var(--pink);font-size:31px;font-weight:400;line-height:1.15">Childcare is More Than a Career<br>at Wattlebrook</h2>
<div class="abs center" style="left:0;top:3137px;width:1200px;font-size:17px;font-weight:600">Children are the heart of our Centres &amp; our people are the soul.</div>
<div class="abs serif" style="left:510px;top:3180px;width:171px;height:31px;background:var(--pink);color:#fff;font-size:11px;display:flex;align-items:center;justify-content:center">Careers at Tiny Sprouts</div>

<svg class="abs" style="left:0;top:3390px" width="1200" height="555" viewBox="0 0 1200 555">
  <path d="M0 90Q300 40 600 70T1200 40V555H0Z" fill="var(--grey)"/>
</svg>
<div class="abs" style="left:575px;top:3462px;width:50px;height:50px;border-radius:50%;background:var(--green);opacity:.8"></div>
<div class="abs serif center" style="left:0;top:3530px;width:1200px;color:var(--brown);font-size:19px">TINY SPROUTS</div>

<div class="abs serif" style="left:199px;top:3608px;font-size:12.5px">Contact Us</div>
<div class="abs" style="left:199px;top:3641px;font-size:14px;font-weight:600">
  <svg width="11" height="11" viewBox="0 0 24 24"><path d="M6.6 10.8a15 15 0 0 0 6.6 6.6l2.2-2.2c.3-.3.7-.4 1-.2 1.1.4 2.3.6 3.6.6.6 0 1 .4 1 1V20c0 .6-.4 1-1 1A17 17 0 0 1 3 4c0-.6.4-1 1-1h3.5c.6 0 1 .4 1 1 0 1.3.2 2.5.6 3.6.1.3 0 .7-.2 1z" fill="#d63b6f"/></svg>&nbsp;123-456-7890</div>
<div class="abs" style="left:199px;top:3676px;font-size:9.5px;font-weight:500">
  <svg width="9" height="8" viewBox="0 0 24 20"><rect x="1" y="2" width="22" height="16" fill="#d63b6f"/><path d="M1 2l11 9 11-9" stroke="#fff" stroke-width="2" fill="none"/></svg>&nbsp;&nbsp;info@tinysprouts.com</div>
<div class="abs" style="left:199px;top:3706px;font-size:9.5px;font-weight:500;line-height:15px;display:flex;gap:10px">
  <svg width="9" height="12" viewBox="0 0 24 32"><path d="M12 0a11 11 0 0 0-11 11c0 8 11 21 11 21s11-13 11-21A11 11 0 0 0 12 0z" fill="#d63b6f"/><circle cx="12" cy="11" r="4" fill="#fff"/></svg>
  <span>28 County Road Lorm, Ipsumj,io,<br>51564 United States</span></div>

<div class="foot-col" style="left:436px">Find Your Closest Centre<br>Childcare NSW<br>Childcare VIC<br>Childcare QLD<br>Childcare ACT<br>Childcare SA</div>
<div class="foot-col" style="left:594px">Childcare and Education<br>Employer Sponsored Care<br>Practical Information<br>News &amp; Advice<br>Our Brand Story<br>FAQs</div>
<div class="foot-col" style="left:775px">Careers at Tiny Sprouts<br>Become a Centre Manager<br>Contact Us<br>Feedback<br>Sign in to KinderLog</div>

<div class="social" style="top:3612px;background:var(--teal)"></div>
<div class="social" style="top:3650px;background:var(--brown)"></div>
<div class="social" style="top:3687px;background:var(--teal)"></div>

<div class="abs" style="left:199px;top:3780px;font-size:9px;font-weight:500">© 2023 <span style="color:var(--pink)">Tiny Sprouts Children &amp; Education</span>. All Right Reserved &nbsp;&nbsp; | &nbsp;&nbsp; Privacy Policy</div>
<svg class="abs" style="left:1091px;top:3770px" width="16" height="18" viewBox="0 0 16 18"><path d="M8 0L16 18L8 13L0 18Z" fill="var(--brown)"/></svg>
<div class="abs" style="left:199px;top:3834px;width:802px;font-size:8.8px;line-height:18px;font-weight:500;color:#333">Childcare Near Me | Daycare Near Me | Early Learning Centre Near Me | Family Daycare Near Me | Pre-School Near Me | Childcare in ACT | Childcare in Queensland | Childcare in NSW | Childcare in Eastern Suburbs, Sydney | Childcare in Inner West, Sydney | Childcare in Northern Sydney | Childcare in North West Sydney | Childcare in Victoria | Childcare in North West Melbourne | Childcare in South East Melbourne</div>

</body>
</html>
```